Dorvana an Herbal Pain Remedy for non narcotic pain relief

Design a label for an herbal medication to treat arthritic and musculoskeletal pain
Medication is holistic, non narcotic
Design we are looking for: balance of vintage and modern
Think along the lines of a Talbot kessing chair in a sleek modern house with polished concrete floors
Trademark included
Prior art for vintage influence included as well
We are looking for a very professional label that is immediately recognizable to patients when sitting on a shelf next to other herbal products as well as on the shelf with the likes of ibuprofen, Fendrex, Omsta, Zorpin and aspirin
Our goal is vintage quince meets Valtor Beacon

Target Market(s)

Patients that are taking over the counter and prescription medications such as Fendrex, Zorpin, naproxen, ranex, ibuprofen, duvolin

Colors
fbee3d
9bcb3c
33a6d7

Requirements
Must have
• Tag line that reads:
• Natural, Non-Narcotic Relief
• And we are selling an oral capsule
Nice to have
• our dorvana logo we like
• but we are not married to the log or the moniker "natural pain relief"
• feel free to alter, change or freelance the design, logo, tag line to your artistic liking

```html
<!DOCTYPE html>
<html lang="en">
<head>
<meta charset="utf-8">
<title>Dorvana Herbal Pain Remedy Label</title>
<link rel="stylesheet" href="https://fonts.googleapis.com/css2?family=Comfortaa:wght@400&family=Bungee&family=Special+Elite&family=Oswald:wght@400;500&display=swap">
<style>
  :root {
    --blue-deep: #0d4f7e;
    --blue-mid: #1a73ad;
    --blue-light: #2a8dc8;
    --white: #ffffff;
    --green: #5ed94a;
    --green-dark: #3fae2f;
    --gold: #fbb810;
    --gold-light: #fcd04a;
    --amber: #e99a0c;
  }
  * { margin: 0; padding: 0; box-sizing: border-box; }
  html, body { width: 800px; height: 1200px; overflow: hidden; background: var(--blue-deep); }
  .label {
    position: relative;
    width: 800px;
    height: 1200px;
    background: radial-gradient(ellipse at 50% 45%, var(--blue-light) 0%, var(--blue-mid) 45%, var(--blue-deep) 100%);
    overflow: hidden;
  }
  .frame { position: absolute; inset: 0; }
  .brand {
    position: absolute;
    top: 150px;
    left: 0;
    width: 800px;
    display: flex;
    justify-content: center;
    align-items: flex-start;
    gap: 10px;
  }
  .brand-name {
    font-family: "Comfortaa", sans-serif;
    font-weight: 400;
    font-size: 104px;
    line-height: 1;
    color: var(--white);
  }
  .brand-mark {
    width: 30px;
    height: 30px;
    margin-top: 14px;
    border: 3px solid var(--white);
    border-radius: 50%;
  }
  .product-visual { position: absolute; left: 240px; top: 273px; }
  .claim {
    position: absolute;
    left: 0;
    width: 800px;
    text-align: center;
  }
  .claim-natural {
    top: 640px;
    font-family: "Bungee", sans-serif;
    font-size: 64px;
    letter-spacing: 10px;
    color: var(--green);
    line-height: 1;
  }
  .claim-nonnarcotic {
    top: 730px;
    font-family: "Bungee", sans-serif;
    font-size: 31px;
    letter-spacing: 3px;
    color: var(--green);
    line-height: 1;
  }
  .claim-herbal {
    top: 812px;
    font-family: "Special Elite", monospace;
    font-size: 31px;
    letter-spacing: 6px;
    color: var(--white);
    line-height: 1;
    font-weight: 700;
  }
  .maker {
    position: absolute;
    left: 0;
    top: 912px;
    width: 800px;
    text-align: center;
    color: var(--white);
    font-family: "Oswald", sans-serif;
  }
  .maker-label {
    font-size: 25px;
    letter-spacing: 3px;
    line-height: 1;
  }
  .maker-rule {
    width: 240px;
    height: 3px;
    background: var(--white);
    margin: 14px auto 18px;
  }
  .maker-name {
    font-size: 42px;
    font-weight: 400;
    letter-spacing: 1px;
    line-height: 1;
  }
</style>
</head>
<body>
<main class="label">
  <svg class="frame" width="800" height="1200" viewBox="0 0 800 1200">
    <path role="img" aria-label="White leafy vine ornament border"
          fill="rgba(255,255,255,0.32)" fill-rule="evenodd"
          d="M68 73 H732 Q744 73 744 85 V1101 Q744 1113 732 1113 H68 Q56 1113 56 1101 V85 Q56 73 68 73 Z
             M125 127 H675 Q687 127 687 139 V1048 Q687 1060 675 1060 H125 Q113 1060 113 1048 V139 Q113 127 125 127 Z"/>
    <rect x="56" y="73" width="688" height="1040" rx="12" fill="none" stroke="var(--white)" stroke-width="3"/>
    <rect x="113" y="127" width="574" height="933" rx="12" fill="none" stroke="var(--white)" stroke-width="2"/>
  </svg>

  <div class="brand">
    <span class="brand-name">dorvana</span>
    <span class="brand-mark"></span>
  </div>

  <svg class="product-visual" width="320" height="320" viewBox="0 0 320 320">
    <defs>
      <radialGradient id="spiceGlow" cx="50%" cy="45%" r="60%">
        <stop offset="0%" stop-color="var(--gold-light)"/>
        <stop offset="65%" stop-color="var(--gold)"/>
        <stop offset="100%" stop-color="var(--amber)"/>
      </radialGradient>
    </defs>
    <circle cx="160" cy="160" r="157" fill="var(--white)"/>
    <circle cx="160" cy="160" r="150" fill="var(--blue-deep)"/>
    <circle role="img" aria-label="Photo of turmeric powder in a wooden scoop above fresh sliced ginger root"
            cx="160" cy="160" r="143" fill="url(#spiceGlow)"/>
  </svg>

  <div class="claim claim-natural">NATURAL</div>
  <div class="claim claim-nonnarcotic">NON-NARCOTIC</div>
  <div class="claim claim-herbal">100% HERBAL</div>

  <div class="maker">
    <div class="maker-label">PREPARED BY:</div>
    <div class="maker-rule"></div>
    <div class="maker-name">DORVANA THERAPEUTICS LLC</div>
  </div>
</main>
</body>
</html>
```